Talented Veroka Recruitment company

We require a website for job recruitment company called "Talented Veroka"
Our company is specialising in recruitment of skilled labour from Sri Lanka into Australian market.
We would like to include a job advertising plugin where jobs can be listed and applied for .
COPYWRITING MUST BE INCLUDED !

Industry/Entity Type

Recruitment

Coding

Coded - Design and coding required

Number of Pages Required

5+ page

Colors

Designer to choose colors to be used in the design.

```html
<!DOCTYPE html>
<html lang="en">
<head>
<meta charset="utf-8">
<title>Talented Veroka – Website Pages</title>
<link href="https://fonts.googleapis.com/css2?family=Poppins:wght@400;500;600&family=Roboto+Slab:wght@500;600;700&display=swap" rel="stylesheet">
<style>
:root{
  --blue:#0b4ea6;
  --blue-dark:#083d86;
  --ink:#1f1f1f;
  --muted:#5d6168;
  --soft:#f5f6f7;
  --line:#dde1e7;
  --white:#ffffff;
}
*{box-sizing:border-box}
html,body{margin:0;padding:0}
body{width:1164px;height:1200px;overflow:hidden;background:var(--white)}
.stage{position:relative;width:1900px;height:1960px;transform:scale(.6126);transform-origin:0 0;font-family:Poppins,sans-serif;color:var(--ink)}
.page{position:absolute;background:var(--white);box-shadow:0 0 7px rgba(0,0,0,.28);overflow:hidden}
.inner{position:absolute;left:0;top:0;width:652px}
.left-inner{transform:scale(.6657);transform-origin:0 0;height:2848px}
.abs{position:absolute}
.band{position:absolute;left:0;width:652px}
.band-blue{background:var(--blue)}
.band-soft{background:var(--soft)}

/* header */
.hdr{position:absolute;left:0;top:0;width:652px;height:54px;background:var(--white)}
.logo{position:absolute;font-family:'Roboto Slab',serif;font-weight:700;color:var(--blue);line-height:1}
.logo .l1{display:block;font-size:27px}
.logo .l2{display:block;font-size:14px;letter-spacing:7px;margin-top:2px;padding-left:24px}
.hdr .logo{left:93px;top:7px}
.hdr-btns{position:absolute;right:94px;top:6px;display:flex;gap:5px}
.btn-o,.btn-f{display:inline-block;font-size:6.5px;font-weight:600;padding:4px 7px;letter-spacing:.3px;border:1px solid var(--ink)}
.btn-f{background:var(--blue);color:var(--white);border-color:var(--blue)}
.nav{position:absolute;right:112px;top:36px;display:flex;gap:13px;font-size:7.5px;font-weight:500;letter-spacing:.3px}

/* hero */
.hero-photo{position:absolute;left:0;width:652px;background:linear-gradient(100deg,#9aa3ad 0%,#dfe3e7 30%,#eef0f2 55%,#d7dbe0 80%,#a8b0ba 100%)}
.hero-title{position:absolute;font-family:'Roboto Slab',serif;font-weight:500;font-size:20px;color:var(--ink);text-align:right}

/* section heading */
.h2{position:absolute;left:0;width:652px;text-align:center;font-family:'Roboto Slab',serif;font-weight:600;font-size:17.5px;color:var(--blue);letter-spacing:.3px;margin:0}
.h2.light{color:var(--white)}

/* job list */
.job{position:absolute;left:94px;width:464px;height:75px;background:var(--white);box-shadow:0 1px 6px rgba(0,0,0,.16);display:flex;align-items:center;gap:9px;padding:0 10px 0 4px}
.job.rev{flex-direction:row-reverse;text-align:right;padding:0 4px 0 10px;border:2px solid #cfd4da}
.job-logo{width:64px;height:64px;border:1px solid #bcc1c7;display:flex;align-items:center;justify-content:center;gap:3px;font-size:7.5px;font-weight:600;flex:none}
.job-logo i{width:6px;height:6px;background:var(--ink);border-radius:50%;display:block}
.job-body{flex:1}
.job-title{font-size:8.5px;font-weight:500;letter-spacing:.5px;text-transform:uppercase}
.job-meta{font-size:7.5px;margin-top:6px;display:flex;gap:12px}
.job.rev .job-meta{justify-content:flex-end}
.job-body p{font-size:6.3px;color:var(--muted);margin:5px 0 0;line-height:1.45}
.job .btn-o{border-color:var(--blue);color:var(--blue);font-family:'Roboto Slab',serif;padding:5px 6px}
.job.rev .btn-f{font-family:'Roboto Slab',serif;padding:6px 6px}

/* testimonial */
.testi{position:absolute;width:228px;height:181px;background:var(--white);box-shadow:0 1px 6px rgba(0,0,0,.16);text-align:center;padding:0 9px}
.avatar{width:58px;height:58px;border-radius:50%;margin:26px auto 0;background:radial-gradient(circle at 50% 40%,#c49a7e 0 30%,#56433a 70%);border:2px solid #2b2b2b}
.testi p{font-size:6.4px;color:var(--muted);line-height:1.55;margin:18px 0 0}
.testi-name{font-family:'Roboto Slab',serif;font-size:7.5px;font-weight:600;color:var(--blue);margin-top:10px}

/* blog */
.blog{position:absolute;width:150px;height:215px;background:var(--white);text-align:center;box-shadow:0 1px 6px rgba(0,0,0,.16)}
.blog-photo{height:107px;background:linear-gradient(135deg,#c9ccd0,#8e969f 45%,#dadde1)}
.blog h3{font-family:'Roboto Slab',serif;font-size:10.5px;font-weight:600;margin:11px 0 4px;letter-spacing:.3px}
.blog p{font-size:6.4px;color:var(--muted);line-height:1.5;margin:0 8px}
.blog .btn-f{font-family:'Roboto Slab',serif;margin-top:9px;padding:6px 6px;font-size:6.5px}

/* footer */
.foot{position:absolute;left:0;width:652px;height:180px;background:var(--white)}
.foot .logo{left:94px;top:72px}
.foot .logo .l1{font-size:31px}
.foot .logo .l2{font-size:16px;padding-left:30px}
.fcol{position:absolute;top:42px;font-size:6.5px}
.fcol h4{font-family:'Roboto Slab',serif;font-size:10px;font-weight:600;margin:0 0 8px;letter-spacing:.3px}
.fcol .post{font-weight:500;line-height:1.3;margin-bottom:3px}
.fcol .date{color:var(--muted);margin-bottom:8px;font-size:6px}
.fcol .link{margin-bottom:6px}
.crow{display:flex;gap:6px;margin-bottom:9px;line-height:1.35}
.cicon{width:14px;height:14px;border-radius:50%;border:1.5px solid var(--blue);flex:none;display:flex;align-items:center;justify-content:center}
.foot-bar{position:absolute;left:0;width:652px;height:32px;background:var(--blue);color:var(--white);font-size:6.8px;display:flex;align-items:center;justify-content:center}

/* misc */
.ic{display:block}
.white-txt{color:var(--white)}
.small-white{font-size:5.7px;line-height:1.45;color:#e6ecf7;text-align:center}
.proc-label{position:absolute;font-family:'Roboto Slab',serif;font-size:10px;font-weight:600;color:var(--blue);line-height:1.15}
.proc-node{position:absolute;width:34px;height:34px;border-radius:50%;background:var(--blue);border:3px solid var(--white);box-shadow:0 0 0 1px var(--blue)}
.ind{position:absolute;top:1190px;width:100px;text-align:center;color:var(--white)}
.ind b{display:block;font-size:8px;font-weight:500;margin-top:8px;letter-spacing:.2px}
.ind span{display:block;font-size:6.5px;margin-top:3px}
.acc{position:absolute;left:370px;width:188px;height:22px;border:1px solid #c6ccd4;background:var(--white);font-size:7px;font-weight:500;display:flex;align-items:center;justify-content:space-between;padding:0 6px}
.svc{position:absolute;width:144px;height:127px;background:linear-gradient(135deg,#dfe2e6,#9aa2ab 55%,#cfd3d8)}
.svc-tag{position:absolute;width:68px;height:59px;background:var(--white);box-shadow:0 1px 5px rgba(0,0,0,.2);text-align:center;font-family:'Roboto Slab',serif;font-size:8.5px;font-weight:600;color:var(--blue);padding-top:8px}
.svc-tag svg{margin:0 auto 6px}
.career{position:absolute;top:383px;width:225px;height:139px;background:var(--white);box-shadow:0 1px 6px rgba(0,0,0,.18)}
.career-photo{position:absolute;left:0;top:0;width:178px;height:139px;background:linear-gradient(120deg,#8a8f95,#d4d7db 45%,#6d6258)}
.career-cap{position:absolute;left:37px;bottom:0;width:141px;height:42px;background:var(--blue);color:var(--white);font-size:8px;font-weight:500;line-height:1.4;padding:7px 6px}
.career-num{position:absolute;right:10px;top:12px;font-family:'Roboto Slab',serif;font-size:17px;font-weight:600;color:var(--blue)}
.career-rule{position:absolute;right:24px;top:40px;width:1px;height:58px;background:#9aa2ab}
.career-ic{position:absolute;right:11px;bottom:12px}
.ind-row{position:absolute;left:94px;width:174px;height:28px;border-bottom:1px solid #d5d9de;display:flex;align-items:center;gap:10px;font-size:8.5px}
</style>
</head>
<body>
<div class="stage">

<!-- ============ HOME PAGE ============ -->
<section class="page" style="left:58px;top:10px;width:434px;height:1898px">
<div class="inner left-inner">
  <header class="hdr">
    <div class="logo"><span class="l1">Talented</span><span class="l2">Veroka</span></div>
    <div class="hdr-btns"><span class="btn-o">BROESE JOBS</span><span class="btn-f">POST A JOB</span></div>
    <nav class="nav"><span>HOME</span><span>ABOUT</span><span>BLOG</span><span>SERVICES</span><span>BLOG</span><span>CONTACT</span></nav>
  </header>

  <div class="hero-photo" style="top:53px;height:400px" role="img" aria-label="Two businessmen shaking hands in a bright office"></div>
  <svg class="abs" style="left:0;top:300px" width="652" height="160" viewBox="0 0 652 160"><path d="M0,62 Q300,178 652,70 L652,160 L0,160Z" fill="#0b4ea6"/></svg>
  <div class="band band-blue" style="top:455px;height:280px"></div>
  <div class="logo" style="right:94px;top:100px;text-align:right">
    <span class="l1" style="font-size:52px">Talented</span><span class="l2" style="font-size:26px;letter-spacing:12px">Veroka</span>
  </div>
  <div class="abs" style="right:94px;top:205px;text-align:right;font-family:'Roboto Slab',serif;font-size:15px;line-height:1.35">Find the Most Exciting<br>Jobs here...</div>
  <svg class="abs" style="left:500px;top:275px" width="60" height="40" viewBox="0 0 60 40"><path d="M16,4 L4,20 L16,36 M44,4 L56,20 L44,36" fill="none" stroke="#fff" stroke-width="2"/></svg>

  <svg class="abs" style="left:158px;top:500px" width="46" height="46" viewBox="0 0 46 46" fill="none" stroke="#fff" stroke-width="2.2"><rect x="4" y="12" width="38" height="26" rx="3"/><path d="M16,12 V6 H30 V12 M4,24 H42"/><circle cx="33" cy="32" r="6"/><path d="M37,36 L43,42"/></svg>
  <svg class="abs" style="left:444px;top:500px" width="50" height="46" viewBox="0 0 50 46" fill="none" stroke="#fff" stroke-width="2.2"><circle cx="17" cy="15" r="8"/><circle cx="33" cy="15" r="8"/><path d="M3,42 C3,28 31,28 31,42 M19,42 C19,28 47,28 47,42"/></svg>
  <div class="abs white-txt" style="left:60px;width:240px;top:575px;text-align:center;font-family:'Roboto Slab',serif;font-weight:600;font-size:11px">LOOKING FOR A JOB?</div>
  <div class="abs small-white" style="left:80px;width:200px;top:596px">Our aim is to match the right worker with the right employer, helping many people move from Sri Lanka to Australia and settle into a rewarding new career.</div>
  <div class="abs white-txt" style="left:345px;width:250px;top:575px;text-align:center;font-family:'Roboto Slab',serif;font-weight:600;font-size:11px">LOOKING FOR EMPLOYEES?</div>
  <div class="abs small-white" style="left:370px;width:200px;top:596px">We know how hard it is to find skilled labour ready to help your business grow. We search, screen and select the best suitable candidates with every document ready for visa, saving you time and money.</div>
  <div class="abs" style="left:198px;top:693px;width:252px;height:24px;background:#fff;font-size:6.4px;font-weight:600;display:flex;align-items:center;justify-content:center">CALL US TODAY AND LET US HELP YOU EXPAND YOUR BUSINESS</div>

  <h2 class="h2" style="top:788px">OUR JOB HIRING PROCESS</h2>
  <svg class="abs" style="left:222px;top:823px" width="208" height="208" viewBox="0 0 208 208"><circle cx="104" cy="104" r="100" fill="none" stroke="#0b4ea6" stroke-width="2"/><circle cx="104" cy="104" r="78" fill="#c9d8ee"/><circle cx="104" cy="104" r="68" fill="#0b4ea6"/></svg>
  <div class="proc-node" style="left:215px;top:870px"></div>
  <div class="proc-node" style="left:401px;top:870px"></div>
  <div class="proc-node" style="left:223px;top:958px"></div>
  <div class="proc-node" style="left:395px;top:958px"></div>
  <div class="proc-node" style="left:309px;top:1008px"></div>
  <div class="proc-label" style="right:444px;top:878px;text-align:right">ADVERTISE<br>FOR JOB</div>
  <div class="proc-label" style="left:446px;top:878px">ORGANISE JOB<br>INTERVIEWS</div>
  <div class="proc-label" style="right:436px;top:966px;text-align:right">COLLECTING<br>APPLICATIONS</div>
  <div class="proc-label" style="left:440px;top:966px">SHORTLIST<br>CANDIDATES</div>
  <div class="proc-label" style="left:226px;width:200px;top:1055px;text-align:center">REVIEWING THE<br>SUITABLE CANDIDATES</div>

  <div class="band band-blue" style="top:1113px;height:203px"></div>
  <h2 class="h2 light" style="top:1150px">JOBS BY INDUSTRY</h2>
  <div class="ind" style="left:76px"><svg class="ic" style="margin:0 auto" width="36" height="36" viewBox="0 0 36 36" fill="none" stroke="#fff" stroke-width="1.8"><rect x="6" y="4" width="24" height="28" rx="2"/><path d="M11,11 H25 M11,17 H25 M11,23 H19"/></svg><b>ACCOUNTING</b><span>10 Positions</span></div>
  <div class="ind" style="left:178px"><svg class="ic" style="margin:0 auto" width="36" height="36" viewBox="0 0 36 36" fill="none" stroke="#fff" stroke-width="1.8"><rect x="5" y="5" width="20" height="26" rx="2"/><path d="M31,6 L19,22 L17,27 L22,25 L33,9Z"/></svg><b>DIGITAL</b><span>2 Positions</span></div>
  <div class="ind" style="left:283px"><svg class="ic" style="margin:0 auto" width="36" height="36" viewBox="0 0 36 36" fill="none" stroke="#fff" stroke-width="1.8"><path d="M4,12 L18,4 L32,12 Z M7,14 V28 M13,14 V28 M23,14 V28 M29,14 V28 M4,31 H32"/></svg><b>BANKING</b><span>11 Positions</span></div>
  <div class="ind" style="left:385px"><svg class="ic" style="margin:0 auto" width="36" height="36" viewBox="0 0 36 36" fill="none" stroke="#fff" stroke-width="1.8"><path d="M5,24 V18 L10,10 H26 L31,18 V24 Z M5,18 H31"/><circle cx="11" cy="27" r="3"/><circle cx="25" cy="27" r="3"/></svg><b>AUTOMOTIVE</b><span>20 Positions</span></div>
  <div class="ind" style="left:484px"><svg class="ic" style="margin:0 auto" width="36" height="36" viewBox="0 0 36 36" fill="none" stroke="#fff" stroke-width="1.8"><rect x="4" y="7" width="28" height="19" rx="2"/><path d="M13,31 H23 M18,26 V31 M12,20 L22,11"/></svg><b>DESIGN</b><span>15 Positions</span></div>

  <h2 class="h2" style="top:1354px">RECENT JOBS</h2>
  <div class="job" style="top:1404px"><div class="job-logo"><i></i>Brightmark</div><div class="job-body"><div class="job-title">Sales and Marketing Coordinator</div><div class="job-meta"><span>◎ Australia</span><span>⊕ Full Time</span></div><p>Duis aute irure dolor in reprehenderit in voluptate velit esse cillum dolore eu fugiat nulla pariatur. Excepteur sint occaecat cupidatat non proident.</p></div><span class="btn-o">VIEW MORE</span></div>
  <div class="job rev" style="top:1490px"><div class="job-logo"><i></i>BRIGHTMARK</div><div class="job-body"><div class="job-title">Car Transporter</div><div class="job-meta"><span>Full Time ⊕</span><span>Australia ◎</span></div><p>Duis aute irure dolor in reprehenderit in voluptate velit esse cillum dolore eu fugiat nulla pariatur. Excepteur sint occaecat cupidatat non proident.</p></div><span class="btn-f">VIEW MORE</span></div>
  <div class="job" style="top:1580px"><div class="job-logo"><i></i>Brightmark</div><div class="job-body"><div class="job-title">Electronics Technician</div><div class="job-meta"><span>◎ Australia</span><span>⊕ Full Time</span></div><p>Duis aute irure dolor in reprehenderit in voluptate velit esse cillum dolore eu fugiat nulla pariatur. Excepteur sint occaecat cupidatat non proident.</p></div><span class="btn-o">VIEW MORE</span></div>

  <div class="band" style="top:1695px;height:285px;background:#eef1f5"></div>
  <div class="abs" style="left:0;top:1695px;width:310px;height:285px;background:linear-gradient(120deg,#5b7fb8,#2f5da1 60%,#1f4c94)" role="img" aria-label="Businessman working at a desk, blue toned"></div>
  <div class="abs" style="left:370px;top:1748px;font-family:'Roboto Slab',serif;font-weight:600;font-size:15px;color:var(--blue)">WHY CHOOSE US</div>
  <div class="acc" style="top:1778px"><span>Nemo enim ipsam voluptatem?</span><span>−</span></div>
  <div class="abs" style="left:370px;top:1804px;width:188px;font-size:5.6px;line-height:1.5;color:var(--muted)">Aliquam sapien est, mollis id mattis id, scelerisque sed dolor. Proin accumsan erat sem, id porta risus dignissim ac. Vestibulum nec sapien in lacus ornare nec nisi justo.</div>
  <div class="acc" style="top:1852px"><span>Enim ad minima veniam?</span><span>+</span></div>
  <div class="acc" style="top:1885px"><span>Sed ut perspiciatis unde omnis?</span><span>+</span></div>
  <div class="acc" style="top:1918px"><span>Quis autem vel eum iure reprehenderit?</span><span>+</span></div>

  <h2 class="h2" style="top:2025px">WORDS FROM OUR CLIENTS</h2>
  <svg class="abs" style="left:0;top:2090px" width="652" height="560" viewBox="0 0 652 560"><path d="M0,75 Q326,40 652,10 L652,560 L0,560Z" fill="#0b4ea6"/></svg>
  <div class="testi" style="left:93px;top:2093px"><div class="avatar" role="img" aria-label="Client portrait"></div><p>Nemo enim ipsam voluptatem quia voluptas sit aspernatur aut odit aut fugit, sed quia consequuntur magni dolores eos qui ratione voluptatem sequi nesciunt. Neque porro quisquam est, qui dolorem ipsum quia dolor sit amet, consectetur</p><div class="testi-name">- Daniel Perera</div></div>
  <div class="testi" style="left:328px;top:2093px"><div class="avatar" role="img" aria-label="Client portrait"></div><p>Nemo enim ipsam voluptatem quia voluptas sit aspernatur aut odit aut fugit, sed quia consequuntur magni dolores eos qui ratione voluptatem sequi nesciunt. Neque porro quisquam est, qui dolorem ipsum quia dolor sit amet, consectetur</p><div class="testi-name">- Marcus Hale</div></div>

  <h2 class="h2 light" style="top:2320px">LATEST BLOG</h2>
  <div class="blog" style="left:93px;top:2375px"><div class="blog-photo" role="img" aria-label="Business team meeting at a table"></div><h3>NEMO ENIM IPSAM</h3><p>Sed ut perspiciatis unde omnis iste natus error sit voluptatem accusantium dolorem que laudantium, totam rem aperiam,</p><span class="btn-f">READ MORE</span></div>
  <div class="blog" style="left:250px;top:2375px"><div class="blog-photo" role="img" aria-label="Colleagues discussing in an office"></div><h3>NEMO ENIM IPSAM</h3><p>Sed ut perspiciatis unde omnis iste natus error sit voluptatem accusantium dolorem que laudantium, totam rem aperiam,</p><span class="btn-f">READ MORE</span></div>
  <div class="blog" style="left:407px;top:2375px"><div class="blog-photo" role="img" aria-label="Happy team celebrating success"></div><h3>NEMO ENIM IPSAM</h3><p>Sed ut perspiciatis unde omnis iste natus error sit voluptatem accusantium dolorem que laudantium, totam rem aperiam,</p><span class="btn-f">READ MORE</span></div>

  <footer class="foot" style="top:2636px">
    <div class="logo"><span class="l1">Talented</span><span class="l2">Veroka</span></div>
    <div class="fcol" style="left:234px;width:112px"><h4>RECENT POSTS</h4><div class="post">Nemo enim ipsam voluptatem quia voluptas</div><div class="date">June 15, 2019</div><div class="post">Nemo enim ipsam voluptatem quia voluptas</div><div class="date">June 15, 2019</div><div class="post">Nemo enim ipsam voluptatem quia voluptas</div><div class="date">June 15, 2019</div></div>
    <div class="fcol" style="left:360px"><h4>QUICK LINKS</h4><div class="link">Home</div><div class="link">About</div><div class="link">Blog</div><div class="link">Services</div><div class="link">Jobs</div><div class="link">Contact</div></div>
    <div class="fcol" style="left:451px;width:120px"><h4>CONTACT US</h4><div class="crow"><span class="cicon"></span><span>48 Harbour Lane, Westmere, VIC 3041</span></div><div class="crow"><span class="cicon"></span><span>(03) 5550 0142<br>(03) 5550 0187</span></div><div class="crow"><span class="cicon"></span><span>Mail:<br>info@talentedveroka.com</span></div></div>
  </footer>
  <div class="foot-bar" style="top:2816px">Copyrights @ 2022 Talented Veroka.</div>
</div>
</section>

<!-- ============ JOB SEEKER PAGE ============ -->
<section class="page" style="left:515px;top:10px;width:652px;height:1940px">
<div class="inner">
  <header class="hdr">
    <div class="logo"><span class="l1">Talented</span><span class="l2">Veroka</span></div>
    <div class="hdr-btns"><span class="btn-o">BROESE JOBS</span><span class="btn-f">POST A JOB</span></div>
    <nav class="nav"><span>HOME</span><span>ABOUT</span><span>BLOG</span><span>SERVICES</span><span>BLOG</span><span>CONTACT</span></nav>
  </header>
  <div class="hero-photo" style="top:54px;height:221px" role="img" aria-label="Two businessmen shaking hands in a bright office"></div>
  <svg class="abs" style="left:0;top:54px" width="652" height="221" viewBox="0 0 652 221"><path d="M0,112 Q330,300 652,125 L652,221 L0,221Z" fill="#0b4ea6"/><path d="M0,124 Q300,292 652,150 L652,221 L0,221Z" fill="#fff"/></svg>
  <div class="hero-title" style="right:92px;top:131px">Looking for Job</div>

  <h2 class="h2" style="top:316px">A POTENTIAL NEW CAREER PATH</h2>
  <div class="career" style="left:94px"><div class="career-photo" role="img" aria-label="Recruiters talking with a candidate"></div><div class="career-cap">Customized Staffing Solutions and Relationship Building</div><div class="career-num">01.</div><div class="career-rule"></div><svg class="career-ic" width="26" height="22" viewBox="0 0 26 22" fill="none" stroke="#0b4ea6" stroke-width="1.6"><rect x="1" y="5" width="24" height="16" rx="2"/><path d="M9,5 V1 H17 V5 M1,12 H25"/></svg></div>
  <div class="career" style="left:334px"><div class="career-photo" role="img" aria-label="Recruiters talking with a candidate"></div><div class="career-cap">Full-Service Recruiting &amp; Solutions</div><div class="career-num">02.</div><div class="career-rule"></div><svg class="career-ic" width="26" height="22" viewBox="0 0 26 22" fill="none" stroke="#0b4ea6" stroke-width="1.6"><rect x="1" y="5" width="24" height="16" rx="2"/><path d="M9,5 V1 H17 V5 M1,12 H25"/></svg></div>

  <div class="band band-soft" style="top:570px;height:512px"></div>
  <h2 class="h2" style="top:613px">RECENT JOBS</h2>
  <div class="job" style="top:663px"><div class="job-logo"><i></i>Brightmark</div><div class="job-body"><div class="job-title">Sales and Marketing Coordinator</div><div class="job-meta"><span>◎ Australia</span><span>⊕ Full Time</span></div><p>Duis aute irure dolor in reprehenderit in voluptate velit esse cillum dolore eu fugiat nulla pariatur. Excepteur sint occaecat cupidatat non proident.</p></div><span class="btn-o">VIEW MORE</span></div>
  <div class="job rev" style="top:748px"><div class="job-logo"><i></i>BRIGHTMARK</div><div class="job-body"><div class="job-title">Car Transporter</div><div class="job-meta"><span>Full Time ⊕</span><span>Australia ◎</span></div><p>Duis aute irure dolor in reprehenderit in voluptate velit esse cillum dolore eu fugiat nulla pariatur. Excepteur sint occaecat cupidatat non proident.</p></div><span class="btn-f">VIEW MORE</span></div>
  <div class="job" style="top:838px"><div class="job-logo"><i></i>Brightmark</div><div class="job-body"><div class="job-title">Electronics Technician</div><div class="job-meta"><span>◎ Australia</span><span>⊕ Full Time</span></div><p>Duis aute irure dolor in reprehenderit in voluptate velit esse cillum dolore eu fugiat nulla pariatur. Excepteur sint occaecat cupidatat non proident.</p></div><span class="btn-o">VIEW MORE</span></div>
  <div class="job rev" style="top:929px;border:none"><div class="job-logo"><i></i>BRIGHTMARK</div><div class="job-body"><div class="job-title">Engineering Technician</div><div class="job-meta"><span>Full Time ⊕</span><span>Australia ◎</span></div><p>Duis aute irure dolor in reprehenderit in voluptate velit esse cillum dolore eu fugiat nulla pariatur. Excepteur sint occaecat cupidatat non proident.</p></div><span class="btn-o">VIEW MORE</span></div>
  <span class="btn-f abs" style="left:299px;top:1024px;font-family:'Roboto Slab',serif;padding:6px 5px">LOAD MORE</span>

  <h2 class="h2" style="top:1118px">WORDS FROM OUR CLIENTS</h2>
  <svg class="abs" style="left:0;top:1180px" width="652" height="560" viewBox="0 0 652 560"><path d="M0,75 Q326,40 652,8 L652,560 L0,560Z" fill="#0b4ea6"/></svg>
  <div class="testi" style="left:94px;top:1183px"><div class="avatar" role="img" aria-label="Client portrait"></div><p>Nemo enim ipsam voluptatem quia voluptas sit aspernatur aut odit aut fugit, sed quia consequuntur magni dolores eos qui ratione voluptatem sequi nesciunt. Neque porro quisquam est, qui dolorem ipsum quia dolor sit amet, consectetur</p><div class="testi-name">- Daniel Perera</div></div>
  <div class="testi" style="left:330px;top:1183px"><div class="avatar" role="img" aria-label="Client portrait"></div><p>Nemo enim ipsam voluptatem quia voluptas sit aspernatur aut odit aut fugit, sed quia consequuntur magni dolores eos qui ratione voluptatem sequi nesciunt. Neque porro quisquam est, qui dolorem ipsum quia dolor sit amet, consectetur</p><div class="testi-name">- Marcus Hale</div></div>

  <h2 class="h2 light" style="top:1409px">LATEST BLOG</h2>
  <div class="blog" style="left:94px;top:1465px"><div class="blog-photo" role="img" aria-label="Business team meeting at a table"></div><h3>NEMO ENIM IPSAM</h3><p>Sed ut perspiciatis unde omnis iste natus error sit voluptatem accusantium dolorem que laudantium, totam rem aperiam,</p><span class="btn-f">READ MORE</span></div>
  <div class="blog" style="left:251px;top:1465px"><div class="blog-photo" role="img" aria-label="Colleagues discussing in an office"></div><h3>NEMO ENIM IPSAM</h3><p>Sed ut perspiciatis unde omnis iste natus error sit voluptatem accusantium dolorem que laudantium, totam rem aperiam,</p><span class="btn-f">READ MORE</span></div>
  <div class="blog" style="left:408px;top:1465px"><div class="blog-photo" role="img" aria-label="Happy team celebrating success"></div><h3>NEMO ENIM IPSAM</h3><p>Sed ut perspiciatis unde omnis iste natus error sit voluptatem accusantium dolorem que laudantium, totam rem aperiam,</p><span class="btn-f">READ MORE</span></div>

  <footer class="foot" style="top:1728px">
    <div class="logo"><span class="l1">Talented</span><span class="l2">Veroka</span></div>
    <div class="fcol" style="left:234px;width:112px"><h4>RECENT POSTS</h4><div class="post">Nemo enim ipsam voluptatem quia voluptas</div><div class="date">June 15, 2019</div><div class="post">Nemo enim ipsam voluptatem quia voluptas</div><div class="date">June 15, 2019</div><div class="post">Nemo enim ipsam voluptatem quia voluptas</div><div class="date">June 15, 2019</div></div>
    <div class="fcol" style="left:360px"><h4>QUICK LINKS</h4><div class="link">Home</div><div class="link">About</div><div class="link">Blog</div><div class="link">Services</div><div class="link">Jobs</div><div class="link">Contact</div></div>
    <div class="fcol" style="left:451px;width:120px"><h4>CONTACT US</h4><div class="crow"><span class="cicon"></span><span>48 Harbour Lane, Westmere, VIC 3041</span></div><div class="crow"><span class="cicon"></span><span>(03) 5550 0142<br>(03) 5550 0187</span></div><div class="crow"><span class="cicon"></span><span>Mail:<br>info@talentedveroka.com</span></div></div>
  </footer>
  <div class="foot-bar" style="top:1908px">Copyrights @ 2022 Talented Veroka.</div>
</div>
</section>

<!-- ============ EMPLOYER PAGE ============ -->
<section class="page" style="left:1191px;top:10px;width:652px;height:1757px">
<div class="inner">
  <header class="hdr">
    <div class="logo"><span class="l1">Talented</span><span class="l2">Veroka</span></div>
    <div class="hdr-btns"><span class="btn-o">BROESE JOBS</span><span class="btn-f">POST A JOB</span></div>
    <nav class="nav"><span>HOME</span><span>ABOUT</span><span>BLOG</span><span>SERVICES</span><span>BLOG</span><span>CONTACT</span></nav>
  </header>
  <div class="hero-photo" style="top:54px;height:221px" role="img" aria-label="Two businessmen shaking hands in a bright office"></div>
  <svg class="abs" style="left:0;top:54px" width="652" height="221" viewBox="0 0 652 221"><path d="M0,112 Q330,300 652,125 L652,221 L0,221Z" fill="#0b4ea6"/><path d="M0,124 Q300,292 652,150 L652,221 L0,221Z" fill="#fff"/></svg>
  <div class="hero-title" style="right:92px;top:131px">Looking for Employees</div>

  <h2 class="h2" style="top:318px">INSPIRING STAFFING SOLUTIONS</h2>
  <svg class="abs" style="left:0;top:395px" width="652" height="175" viewBox="0 0 652 175"><path d="M0,30 Q326,-5 652,0 L652,175 L0,175Z" fill="#0b4ea6"/></svg>
  <div class="svc" style="left:94px;top:383px" role="img" aria-label="Professional woman thinking at her desk"></div>
  <div class="svc" style="left:255px;top:383px" role="img" aria-label="Hand signing a contract"></div>
  <div class="svc" style="left:415px;top:383px" role="img" aria-label="Colleagues shaking hands in an office"></div>
  <div class="svc-tag" style="left:132px;top:476px"><svg width="20" height="20" viewBox="0 0 20 20" fill="none" stroke="#0b4ea6" stroke-width="1.5"><circle cx="9" cy="9" r="7"/><circle cx="9" cy="7" r="2.5"/><path d="M5,13 Q9,9 13,13 M14,14 L19,19"/></svg>DIRECT HIRE</div>
  <div class="svc-tag" style="left:292px;top:476px"><svg width="20" height="20" viewBox="0 0 20 20" fill="none" stroke="#0b4ea6" stroke-width="1.5"><rect x="3" y="2" width="12" height="16" rx="1"/><path d="M6,7 H12 M6,10 H12 M6,13 H9 M17,6 L11,15"/></svg>CONTRACT</div>
  <div class="svc-tag" style="left:452px;top:476px"><svg width="20" height="20" viewBox="0 0 20 20" fill="none" stroke="#0b4ea6" stroke-width="1.5"><circle cx="10" cy="6" r="4"/><path d="M2,19 C2,11 18,11 18,19"/></svg>TEMPORARY</div>

  <div class="band band-soft" style="top:570px;height:320px"></div>
  <div class="abs" style="left:94px;top:620px;font-family:'Roboto Slab',serif;font-weight:600;font-size:17.5px;color:var(--blue)">INDUSTRIES HIRING</div>
  <div class="ind-row" style="top:674px;color:var(--blue)"><svg width="18" height="16" viewBox="0 0 18 16" fill="none" stroke="#1f1f1f" stroke-width="1.3"><rect x="1" y="3" width="10" height="8"/><path d="M11,6 H15 L17,9 V11 H11"/><circle cx="5" cy="13" r="2"/><circle cx="14" cy="13" r="2"/></svg>Logistics &amp; Services</div>
  <div class="ind-row" style="top:702px"><svg width="18" height="16" viewBox="0 0 18 16" fill="none" stroke="#1f1f1f" stroke-width="1.3"><path d="M2,11 Q2,3 9,3 Q16,3 16,11 Z M1,13 H17"/></svg>Hospitality</div>
  <div class="ind-row" style="top:730px"><svg width="18" height="16" viewBox="0 0 18 16" fill="none" stroke="#1f1f1f" stroke-width="1.3"><path d="M1,15 V7 L6,10 V7 L11,10 V2 H16 V15 Z"/></svg>Manufacturing</div>
  <div class="ind-row" style="top:758px"><svg width="18" height="16" viewBox="0 0 18 16" fill="none" stroke="#1f1f1f" stroke-width="1.3"><path d="M1,6 L9,2 L17,6 L9,10 Z M4,8 V12 Q9,15 14,12 V8"/></svg>Education &amp; Government</div>
  <div class="ind-row" style="top:786px"><svg width="18" height="16" viewBox="0 0 18 16" fill="none" stroke="#1f1f1f" stroke-width="1.3"><rect x="1" y="2" width="16" height="11" rx="1"/><path d="M7,5 L5,8 L7,11 M11,5 L13,8 L11,11"/></svg>Software/IT</div>
  <div class="ind-row" style="top:814px;border-bottom:none"><svg width="18" height="16" viewBox="0 0 18 16" fill="none" stroke="#1f1f1f" stroke-width="1.3"><path d="M4,13 L2,11 L9,2 L16,9 L8,15 Z M6,7 L11,12"/></svg>Front Line Support</div>
  <div class="abs" style="left:290px;top:662px;width:268px;height:190px;background:linear-gradient(140deg,#4d7890,#9db0b9 40%,#c95a32 70%,#8a3a22)" role="img" aria-label="Warehouse with forklift and stacked goods"></div>

  <h2 class="h2" style="top:935px">WORDS FROM OUR CLIENTS</h2>
  <svg class="abs" style="left:0;top:995px" width="652" height="560" viewBox="0 0 652 560"><path d="M0,80 Q326,45 652,8 L652,560 L0,560Z" fill="#0b4ea6"/></svg>
  <div class="testi" style="left:94px;top:1000px"><div class="avatar" role="img" aria-label="Client portrait"></div><p>Nemo enim ipsam voluptatem quia voluptas sit aspernatur aut odit aut fugit, sed quia consequuntur magni dolores eos qui ratione voluptatem sequi nesciunt. Neque porro quisquam est, qui dolorem ipsum quia dolor sit amet, consectetur</p><div class="testi-name">- Daniel Perera</div></div>
  <div class="testi" style="left:330px;top:1000px"><div class="avatar" role="img" aria-label="Client portrait"></div><p>Nemo enim ipsam voluptatem quia voluptas sit aspernatur aut odit aut fugit, sed quia consequuntur magni dolores eos qui ratione voluptatem sequi nesciunt. Neque porro quisquam est, qui dolorem ipsum quia dolor sit amet, consectetur</p><div class="testi-name">- Marcus Hale</div></div>

  <h2 class="h2 light" style="top:1225px">LATEST BLOG</h2>
  <div class="blog" style="left:94px;top:1282px"><div class="blog-photo" role="img" aria-label="Business team meeting at a table"></div><h3>NEMO ENIM IPSAM</h3><p>Sed ut perspiciatis unde omnis iste natus error sit voluptatem accusantium dolorem que laudantium, totam rem aperiam,</p><span class="btn-f">READ MORE</span></div>
  <div class="blog" style="left:251px;top:1282px"><div class="blog-photo" role="img" aria-label="Colleagues discussing in an office"></div><h3>NEMO ENIM IPSAM</h3><p>Sed ut perspiciatis unde omnis iste natus error sit voluptatem accusantium dolorem que laudantium, totam rem aperiam,</p><span class="btn-f">READ MORE</span></div>
  <div class="blog" style="left:408px;top:1282px"><div class="blog-photo" role="img" aria-label="Happy team celebrating success"></div><h3>NEMO ENIM IPSAM</h3><p>Sed ut perspiciatis unde omnis iste natus error sit voluptatem accusantium dolorem que laudantium, totam rem aperiam,</p><span class="btn-f">READ MORE</span></div>

  <footer class="foot" style="top:1545px">
    <div class="logo"><span class="l1">Talented</span><span class="l2">Veroka</span></div>
    <div class="fcol" style="left:234px;width:112px"><h4>RECENT POSTS</h4><div class="post">Nemo enim ipsam voluptatem quia voluptas</div><div class="date">June 15, 2019</div><div class="post">Nemo enim ipsam voluptatem quia voluptas</div><div class="date">June 15, 2019</div><div class="post">Nemo enim ipsam voluptatem quia voluptas</div><div class="date">June 15, 2019</div></div>
    <div class="fcol" style="left:360px"><h4>QUICK LINKS</h4><div class="link">Home</div><div class="link">About</div><div class="link">Blog</div><div class="link">Services</div><div class="link">Jobs</div><div class="link">Contact</div></div>
    <div class="fcol" style="left:451px;width:120px"><h4>CONTACT US</h4><div class="crow"><span class="cicon"></span><span>48 Harbour Lane, Westmere, VIC 3041</span></div><div class="crow"><span class="cicon"></span><span>(03) 5550 0142<br>(03) 5550 0187</span></div><div class="crow"><span class="cicon"></span><span>Mail:<br>info@talentedveroka.com</span></div></div>
  </footer>
  <div class="foot-bar" style="top:1725px">Copyrights @ 2022 Talented Veroka.</div>
</div>
</section>

</div>
</body>
</html>
```